Business Card, Stationary, and Invoice
PuzzleHarbor
Business Card, Stationary, and Invoice - Games
Creative Brief
Use specific fonts
Use logo font..or similar if logo font doesn't look good.
Bright & Fun-filled
Lyle Ostrand
Owner
84 Brackett Lane Alder Falls, VT 05467
lyle@puzzleharbor-example.com
www.puzzleharbor-example.com
Require business card, stationary, and invoice.

```html
<!DOCTYPE html>
<html lang="en">
<head>
<meta charset="utf-8">
<title>PuzzleHarbor business card</title>
<link rel="stylesheet" href="https://fonts.googleapis.com/css2?family=Open+Sans:wght@400;600;700&display=swap">
<style>
  :root {
    --backdrop: #e9e6e1;
    --card: #ffffff;
    --gold: #b8923f;
    --gold-light: #dcc48a;
    --grey: #8d8d8d;
    --grey-light: #d9d9d9;
    --ink: #3a3a3a;
  }
  html, body {
    margin: 0;
    width: 1200px;
    height: 463px;
    overflow: hidden;
    background: var(--backdrop);
    font-family: "Open Sans", Arial, sans-serif;
  }
  .stage { position: relative; width: 1200px; height: 463px; }
  .card {
    position: absolute;
    top: 104px;
    width: 510px;
    height: 276px;
    background: var(--card);
    border-radius: 18px;
    overflow: hidden;
    box-shadow: 0 6px 18px rgba(0,0,0,.18);
  }
  .card--front { left: 96px; }
  .card--back { left: 636px; }
  .swoosh { position: absolute; left: 0; top: 0; width: 510px; height: 276px; }
  .brand {
    position: absolute;
    display: flex;
    align-items: center;
    gap: 8px;
    font-weight: 700;
    font-size: 30px;
    line-height: 1;
    color: var(--gold);
    white-space: nowrap;
  }
  .brand-dot {
    width: 14px; height: 14px; border-radius: 50%;
    background: var(--gold);
  }
  .card--front .brand { left: 34px; top: 82px; }
  .card--back .brand { left: 0; right: 0; top: 86px; justify-content: center; }
  .divider {
    position: absolute; left: 306px; top: 40px;
    width: 1px; height: 100px; background: var(--grey-light);
  }
  .contact {
    position: absolute; left: 316px; top: 42px;
    font-size: 10.5px; line-height: 15px; color: var(--ink);
    white-space: nowrap;
  }
  .contact .address { margin-bottom: 4px; }
  .contact b { font-weight: 600; color: var(--grey); display: inline-block; width: 14px; }
  .person {
    position: absolute; left: 140px; top: 192px;
    font-size: 16px; line-height: 20px; color: var(--gold); font-weight: 600;
    white-space: nowrap;
  }
  .person .role {
    color: var(--grey); font-weight: 400; font-size: 13px;
    margin-left: 10px; padding-left: 10px; border-left: 1px solid var(--grey-light);
  }
</style>
</head>
<body>
<div class="stage">

  <section class="card card--front">
    <svg class="swoosh" viewBox="0 0 510 276" aria-hidden="true">
      <defs>
        <linearGradient id="fade-front" x1="0" y1="0" x2="0" y2="1">
          <stop offset="0" stop-color="#ffffff"/>
          <stop offset="1" stop-color="#cfcfcf"/>
        </linearGradient>
      </defs>
      <path d="M0 230 C120 218 310 214 510 172 L510 276 L0 276 Z" fill="url(#fade-front)"/>
      <path d="M0 242 C150 230 340 222 510 180 L510 192 C340 236 150 244 0 254 Z" fill="var(--gold)"/>
      <path d="M0 258 C170 248 350 240 510 204 L510 210 C350 250 170 258 0 264 Z" fill="var(--gold-light)"/>
    </svg>
    <div class="brand"><span class="brand-dot"></span>PuzzleHarbor</div>
    <div class="divider"></div>
    <div class="contact">
      <div class="address">84 Brackett Lane<br>Alder Falls, VT 05467</div>
      <div><b>C</b>: 802-555-0137</div>
      <div><b>E</b>: lyle@puzzleharbor-example.com</div>
      <div><b>W</b>: www.puzzleharbor-example.com</div>
    </div>
    <div class="person">Lyle Ostrand<span class="role">Owner</span></div>
  </section>

  <section class="card card--back">
    <svg class="swoosh" viewBox="0 0 510 276" aria-hidden="true">
      <defs>
        <linearGradient id="fade-back" x1="0" y1="0" x2="0" y2="1">
          <stop offset="0" stop-color="#ffffff"/>
          <stop offset="1" stop-color="#cfcfcf"/>
        </linearGradient>
      </defs>
      <path d="M0 230 C120 218 310 214 510 172 L510 276 L0 276 Z" fill="url(#fade-back)"/>
      <path d="M0 242 C150 230 340 222 510 180 L510 192 C340 236 150 244 0 254 Z" fill="var(--gold)"/>
      <path d="M0 258 C170 248 350 240 510 204 L510 210 C350 250 170 258 0 264 Z" fill="var(--gold-light)"/>
    </svg>
    <div class="brand"><span class="brand-dot"></span>PuzzleHarbor</div>
  </section>

</div>
</body>
</html>
```